The Velvet Magpie business card

I need a business card for my makeup artist business. I specialise in bridal, glamour, formal and special occasion makeup.
I am a mobile makeup artist who caters for every from nowra to sydney.
I do the following services:
Bridal makeup
airbrush makeup
special occasion
formals
hens nights/ girls night
makeup lesson
makeup for all ages from flower girl to Nanna of the bride!
photoshoot makeup
SPFX

I would like the card to portray a very professional sleek makeup business. I would also like another version of the card directed especially towards brides.

Please see my website to understand colours etc www.thevelvetmagpie.com

The Velvet Magpie
Professional Makeup Artist
Marisol Dunkel
0471829304
info@thevelvetmagpie.com
www.thevelvetmagpie.com
www.facebook.com/thevelvetmagpie

```html
<!DOCTYPE html>
<html lang="en">
<head>
<meta charset="utf-8">
<title>The Velvet Magpie – Business Card</title>
<link rel="stylesheet" href="https://fonts.googleapis.com/css2?family=Exo+2:wght@300;400&display=swap">
<style>
  :root {
    --magenta: #dc1478;
    --white: #ffffff;
    --backdrop: #efeae3;
    --card-w: 450px;
    --card-h: 797px;
  }
  * { box-sizing: border-box; margin: 0; padding: 0; }
  html, body {
    width: 1200px; height: 1137px; overflow: hidden;
    background: var(--backdrop);
    font-family: "Exo 2", sans-serif;
  }
  .canvas { position: relative; width: 1200px; height: 1137px; }
  .card {
    position: absolute; top: 162px;
    width: var(--card-w); height: var(--card-h);
    background: var(--magenta);
    overflow: hidden;
    box-shadow: 0 6px 18px rgba(0,0,0,.18);
  }
  .card--front { left: 106px; }
  .card--back { left: 644px; }

  .stripe { position: absolute; left: 0; width: 100%; background: var(--white); }
  .stripe--top { top: 52px; height: 27px; }
  .stripe--bottom { top: 720px; height: 27px; }
  .logo-band {
    position: absolute; left: 0; top: 111px; width: 100%; height: 102px;
    background: var(--white);
    display: flex; align-items: center; justify-content: center;
  }
  .brand-name {
    color: var(--magenta); font-weight: 400;
    text-transform: uppercase; letter-spacing: 3px; white-space: nowrap;
  }
  .logo-band .brand-name { font-size: 34px; }

  .owner { position: absolute; top: 280px; width: 100%; text-align: center; color: var(--white); }
  .owner-name { font-size: 32px; font-weight: 300; letter-spacing: 1px; text-transform: uppercase; }
  .owner-role { font-size: 17px; font-weight: 300; margin-top: 6px; }

  .contact-row {
    position: absolute; left: 88px;
    display: flex; align-items: center; gap: 14px;
    color: var(--white); font-size: 17px; font-weight: 300; line-height: 22px;
  }
  .contact-row svg { flex: none; width: 32px; height: 32px; }
  .contact-row--phone { top: 391px; font-size: 19px; }
  .contact-row--web { top: 451px; }
  .contact-row--social { top: 518px; }

  .back-band { position: absolute; left: 0; top: 211px; width: 100%; height: 275px; }
  .back-band .brand-name {
    position: absolute; left: 0; top: 0; width: 100%; height: 100%;
    display: flex; align-items: center; justify-content: center;
    font-size: 38px;
  }
</style>
</head>
<body>
<main class="canvas">

  <section class="card card--front" aria-label="Card front">
    <div class="stripe stripe--top"></div>
    <div class="logo-band"><span class="brand-name">The Velvet Magpie</span></div>

    <div class="owner">
      <p class="owner-name">Marisol Dunkel</p>
      <p class="owner-role">Professional Makeup Artist</p>
    </div>

    <div class="contact-row contact-row--phone">
      <svg viewBox="0 0 32 32" aria-hidden="true">
        <path fill="#fff" d="M3 11c0-4 6-6 13-6s13 2 13 6v2h-6v-3c-2-1-4-1-7-1s-5 0-7 1v3H3z"/>
        <path fill="#fff" d="M10 13h12l5 8v6H5v-6z"/>
        <circle cx="16" cy="20" r="3" fill="#dc1478"/>
      </svg>
      <span>0471829304</span>
    </div>

    <div class="contact-row contact-row--web">
      <svg viewBox="0 0 32 32" aria-hidden="true" fill="none" stroke="#fff" stroke-width="2">
        <circle cx="16" cy="16" r="13"/>
        <ellipse cx="16" cy="16" rx="6" ry="13"/>
        <line x1="3" y1="16" x2="29" y2="16"/>
        <line x1="5" y1="9" x2="27" y2="9"/>
        <line x1="5" y1="23" x2="27" y2="23"/>
      </svg>
      <span>info@thevelvetmagpie.com<br>www.thevelvetmagpie.com</span>
    </div>

    <div class="contact-row contact-row--social">
      <svg viewBox="0 0 32 32" aria-hidden="true"><circle cx="16" cy="16" r="9" fill="#fff"/></svg>
      <span>thevelvetmagpie</span>
    </div>

    <div class="stripe stripe--bottom"></div>
  </section>

  <section class="card card--back" aria-label="Card back">
    <div class="back-band">
      <svg width="450" height="275" viewBox="0 0 450 275" aria-hidden="true">
        <rect width="450" height="275" fill="#fff"/>
        <polygon points="264,33 450,33 450,59" fill="#dc1478"/>
        <polygon points="0,211 243,240 0,242" fill="#dc1478"/>
      </svg>
      <span class="brand-name">The Velvet Magpie</span>
    </div>
  </section>

</main>
</body>
</html>
```